TRV Consulting Website Design
New Website for Consulting company
Project: TRV Consulting Website Design
TRV Consulting Website Design - Consulting
Creative Brief
Consulting
www.trvconsulting-example.com
Logistics consulting focused in Bulk Logistics, Freight Rail, Energy and Chemical sectors with Investment Advisory expertise in the respective sectors. An expert team of industry veterans who partner with clients to design custom logistics solutions with extensive experience in logistics infrastructure design, supply chain assessments, strategic planning, and due diligence projects.
Likes: Clean, crisp, professional imagery Dislikes: Too much text, cluttered, busy sights
Modern
You choose
top
http://www.morwayfreight-example.com/
We have a newly designed logo which we want to use. We are open to changing the colors in the logo as well. Also, the design must be mobile friendly and will be implemented in Bootstrap 3.
torvell torvell
Don't focus on tanker trains and cars Don't focus on human hands

```html
<!DOCTYPE html>
<html lang="en">
<head>
<meta charset="utf-8">
<title>TRV Consulting</title>
<link rel="stylesheet" href="https://fonts.googleapis.com/css2?family=Open+Sans:ital,wght@0,400;0,600;0,700;1,700&display=swap">
<style>
  :root {
    --navy: #0d3c5c;
    --navy-dark: #082b44;
    --orange: #f39a1e;
    --white: #ffffff;
    --page: #eeeeee;
    --card-text: #555555;
    --footer: #4a4a4a;
    --footer-text: #d8d8d8;
    --arrow-bg: rgba(80, 80, 80, 0.75);
  }
  * { box-sizing: border-box; margin: 0; padding: 0; }
  html, body { width: 1200px; height: 998px; overflow: hidden; }
  body {
    position: relative;
    font-family: "Open Sans", Arial, sans-serif;
    background: linear-gradient(#f7f7f7, #e3e3e3);
  }

  .site-header {
    position: absolute; left: 0; top: 0; width: 1200px; height: 143px;
    background: var(--white);
  }
  .brand {
    position: absolute; left: 130px; top: 40px;
    display: flex; align-items: center; gap: 14px;
  }
  .brand-square { width: 44px; height: 44px; background: var(--orange); }
  .brand-name {
    font-weight: 700; font-size: 32px; color: var(--navy); letter-spacing: 0.5px;
  }
  .phone-badge {
    position: absolute; left: 836px; top: 16px; height: 44px; width: 230px;
    display: flex; align-items: stretch;
  }
  .phone-icon {
    width: 52px; background: var(--orange);
    display: flex; align-items: center; justify-content: center;
    clip-path: polygon(12% 0, 100% 0, 88% 100%, 0 100%);
  }
  .phone-number {
    flex: 1; margin-left: -4px; background: var(--navy); color: var(--white);
    font-weight: 600; font-size: 19px; display: flex; align-items: center; justify-content: center;
    clip-path: polygon(6% 0, 100% 0, 94% 100%, 0 100%);
  }
  .main-nav {
    position: absolute; left: 437px; top: 86px;
    display: flex; gap: 30px; list-style: none;
  }
  .main-nav a {
    text-decoration: none; font-weight: 600; font-size: 20px; color: var(--navy); letter-spacing: 0.3px;
  }
  .main-nav a.active { color: var(--orange); }

  .hero {
    position: absolute; left: 0; top: 143px; width: 1200px; height: 418px;
  }
  .hero-photo {
    position: absolute; inset: 0;
    background: linear-gradient(100deg, #cfd6dc 0%, #e9eef2 35%, #b8c3cc 60%, #dde4ea 100%);
  }
  .hero-shade {
    position: absolute; left: 0; right: 0; bottom: 0; height: 120px;
    background: linear-gradient(rgba(0,0,0,0), rgba(0,0,0,0.55));
  }
  .hero-caption {
    position: absolute; left: 159px; top: 352px;
    color: var(--white); font-style: italic; font-weight: 700; font-size: 27px; letter-spacing: 0.5px;
  }
  .hero-arrow {
    position: absolute; top: 187px; width: 42px; height: 36px; background: var(--arrow-bg);
    display: flex; align-items: center; justify-content: center;
  }
  .hero-arrow.prev { left: 14px; }
  .hero-arrow.next { right: 14px; }

  .feature-card {
    position: absolute; top: 604px; width: 286px; height: 300px;
    background: var(--white); box-shadow: 0 2px 5px rgba(0,0,0,0.18);
  }
  .feature-card:nth-of-type(1) { left: 130px; }
  .feature-card:nth-of-type(2) { left: 456px; }
  .feature-card:nth-of-type(3) { left: 782px; }
  .card-title {
    height: 46px; background: var(--navy); color: var(--white);
    font-weight: 700; font-size: 21px; text-align: center; line-height: 46px; letter-spacing: 0.4px;
  }
  .card-image { margin: 14px 10px 0; height: 151px; }
  .card-image.about { background: linear-gradient(120deg, #c9b8a8, #eef0f2 50%, #7d8590); }
  .card-image.services { background: linear-gradient(120deg, #7a2a22, #c9a070 45%, #6f7c88); }
  .card-image.insights { background: linear-gradient(180deg, #5d6f9a, #c08868 55%, #4c5a3e); }
  .card-text {
    margin: 8px 10px 0; font-size: 12.5px; line-height: 18px; color: var(--card-text);
  }
  .card-more {
    position: absolute; left: 123px; bottom: -8px; width: 40px; height: 35px;
    background: var(--orange); display: flex; align-items: center; justify-content: center;
  }

  .site-footer {
    position: absolute; left: 0; top: 950px; width: 1200px; height: 48px; background: var(--footer);
  }
  .copyright {
    position: absolute; left: 135px; top: 15px; font-size: 12px; color: var(--footer-text);
  }
  .social {
    position: absolute; left: 890px; top: 12px; display: flex; gap: 18px; list-style: none;
  }
  .social li { width: 24px; height: 24px; border-radius: 50%; background: #2f2f2f; }
</style>
</head>
<body>
  <header class="site-header">
    <div class="brand">
      <span class="brand-square"></span>
      <span class="brand-name">TRV Consulting</span>
    </div>
    <div class="phone-badge">
      <span class="phone-icon">
        <svg width="20" height="20" viewBox="0 0 24 24" aria-hidden="true">
          <path fill="#fff" d="M6.6 10.8a15.1 15.1 0 0 0 6.6 6.6l2.2-2.2c.3-.3.7-.4 1-.2 1.1.4 2.3.6 3.6.6.6 0 1 .4 1 1V20c0 .6-.4 1-1 1A17 17 0 0 1 3 4c0-.6.4-1 1-1h3.5c.6 0 1 .4 1 1 0 1.3.2 2.5.6 3.6.1.3 0 .7-.2 1z"/>
        </svg>
      </span>
      <span class="phone-number">+1-555-014-2290</span>
    </div>
    <nav>
      <ul class="main-nav">
        <li><a class="active" href="#">HOME</a></li>
        <li><a href="#">ABOUT US</a></li>
        <li><a href="#">OUR SERVICES</a></li>
        <li><a href="#">INSIGHTS</a></li>
        <li><a href="#">CONTACT US</a></li>
      </ul>
    </nav>
  </header>

  <section class="hero">
    <div class="hero-photo" role="img" aria-label="Photo of a business team in suits reviewing documents in a bright office"></div>
    <div class="hero-shade"></div>
    <p class="hero-caption">WE ARE LOGISTICS CONSULTING COMPANY</p>
    <span class="hero-arrow prev">
      <svg width="12" height="16" viewBox="0 0 12 16" aria-hidden="true"><path d="M9 2 3 8l6 6" fill="none" stroke="#fff" stroke-width="2.5"/></svg>
    </span>
    <span class="hero-arrow next">
      <svg width="12" height="16" viewBox="0 0 12 16" aria-hidden="true"><path d="M3 2l6 6-6 6" fill="none" stroke="#fff" stroke-width="2.5"/></svg>
    </span>
  </section>

  <article class="feature-card">
    <h2 class="card-title">ABOUT TRV</h2>
    <div class="card-image about" role="img" aria-label="Photo of consultants meeting together"></div>
    <p class="card-text">Lorem ipsum dolor sit amet, consectetuere adipiscing elit, sed diam nonummy.</p>
    <a class="card-more" href="#"><svg width="16" height="16" viewBox="0 0 16 16" aria-hidden="true"><path d="M8 2v12M2 8h12" stroke="#fff" stroke-width="3"/></svg></a>
  </article>
  <article class="feature-card">
    <h2 class="card-title">OUR SERVICES</h2>
    <div class="card-image services" role="img" aria-label="Photo of rail workers beside a freight locomotive"></div>
    <p class="card-text">Lorem ipsum dolor sit amet, consectetuere adipiscing elit, sed diam nonummy.</p>
    <a class="card-more" href="#"><svg width="16" height="16" viewBox="0 0 16 16" aria-hidden="true"><path d="M8 2v12M2 8h12" stroke="#fff" stroke-width="3"/></svg></a>
  </article>
  <article class="feature-card">
    <h2 class="card-title">INSIGHTS</h2>
    <div class="card-image insights" role="img" aria-label="Photo of an industrial freight terminal at dusk"></div>
    <p class="card-text">Lorem ipsum dolor sit amet, consectetuere adipiscing elit, sed diam nonummy.</p>
    <a class="card-more" href="#"><svg width="16" height="16" viewBox="0 0 16 16" aria-hidden="true"><path d="M8 2v12M2 8h12" stroke="#fff" stroke-width="3"/></svg></a>
  </article>

  <footer class="site-footer">
    <p class="copyright">Copyright © 2015 TRV Consulting. All right reserved.</p>
    <ul class="social">
      <li></li><li></li><li></li><li></li><li></li><li></li>
    </ul>
  </footer>
</body>
</html>
```